Flyer for annual KESTREL SUMMIT 2020

I would like a church event flyer designed. The event is called "KESTREL SUMMIT 2020". I am looking for a professional, yet catchy design that uses our brand colors and logo creatively while communicating key information of the event effectively.

1. The logo is attached in two color formats. The designer has the choice to use them as he/she want.

2. The location of the event is: Harlow Community Center, 239 Fennimore Street, Portland, ME 04117

3. Time and date of event. The designer can organize and format the date and time as he/she pleases.
Thursday December 31st @ 6:30PM
Friday January 1st @ 6:30PM
Saturday 2nd @ 6:30PM
Sunday 3rd @ 4:30PM

4. The topic of the event is "In Fire and On Fire". The designer is free to use this phrase as he/she pleases to create a good composition.

5. Speaker: Prophet Marcus Olunde (2 pictures of the speaker to choose from are attached)

6. Contact information: contact@brightmeadowfold.org - Telephone number: 207 583 2914

7. I would also like the following three words on the flyer. These words describe the focus of the event: FIRE, REVIVAL, PROPHETIC

Target Market(s)

Young adults

Font styles to use
Sans Serif

Requirements
Must have
• Logo, speaker's picture
Should not have
• cross image, church image

```html
<!DOCTYPE html>
<html lang="en">
<head>
<meta charset="utf-8">
<title>Kestrel Summit 2020 Flyer</title>
<link href="https://fonts.googleapis.com/css2?family=Poppins:wght@800;900&family=Rubik:wght@400;500;700;900&display=swap" rel="stylesheet">
<style>
  :root {
    --navy: #0c3556;
    --navy-deep: #071f36;
    --orange: #f08a1c;
    --orange-deep: #e0701a;
    --white: #ffffff;
    --paper: #f3f4f6;
    --ink: #0f2a44;
    --bg: #e4e4e4;
  }
  * { box-sizing: border-box; margin: 0; padding: 0; }
  html, body { width: 1200px; height: 1128px; overflow: hidden; background: var(--bg); }
  body { font-family: "Rubik", sans-serif; }

  .flyer {
    position: absolute; left: 220px; top: 26px;
    width: 760px; height: 1076px; overflow: hidden;
    background: linear-gradient(180deg, var(--navy) 0%, var(--navy-deep) 80%);
  }
  .flyer-shapes { position: absolute; inset: 0; width: 760px; height: 1076px; }

  .event-title {
    position: absolute; left: 0; width: 760px; top: 36px; text-align: center;
    font-family: "Poppins", sans-serif; font-weight: 900; font-size: 116px; line-height: 1;
    letter-spacing: 1px;
    background: linear-gradient(180deg, #ffffff 0%, #e3e5e8 45%, #a9adb3 100%);
    -webkit-background-clip: text; background-clip: text; color: transparent;
    filter: drop-shadow(3px 4px 0 #062036);
  }

  .title-bar {
    position: absolute; left: 81px; top: 179px; width: 589px; height: 62px;
    border-radius: 31px; background: linear-gradient(90deg, var(--orange-deep), var(--orange));
  }
  .title-bar .summit {
    position: absolute; left: 44px; top: 0; line-height: 62px;
    font-weight: 900; font-size: 50px; color: var(--white); letter-spacing: 1px;
  }
  .title-bar .year {
    position: absolute; right: 0; top: 0; width: 172px; height: 62px; border-radius: 31px;
    background: linear-gradient(90deg, #dfe3e8, #ffffff);
    text-align: center; line-height: 62px;
    font-weight: 900; font-size: 50px; color: var(--navy);
  }

  .focus-label {
    position: absolute; width: 140px; text-align: center;
    font-weight: 500; font-size: 16px; color: var(--navy); letter-spacing: .5px;
  }

  .theme {
    position: absolute; left: 54px; top: 436px;
    font-weight: 900; font-size: 56px; line-height: 58px; color: var(--orange);
  }
  .divider { position: absolute; left: 56px; top: 566px; width: 382px; height: 1px; background: #7f93a8; }

  .schedule { position: absolute; left: 56px; top: 580px; color: var(--white); }
  .schedule h2 { font-weight: 700; font-size: 27px; line-height: 32px; margin-bottom: 2px; }
  .schedule p { font-weight: 400; font-size: 21px; line-height: 27.5px; }
  .schedule strong { font-weight: 700; }

  .host { position: absolute; left: 58px; top: 800px; display: flex; align-items: center; gap: 12px; }
  .host .mark { width: 20px; height: 20px; border-radius: 50%; background: var(--orange); }
  .host .name { font-weight: 500; font-size: 40px; color: var(--white); letter-spacing: 2px; }

  .footer-band { position: absolute; left: 0; top: 896px; width: 760px; height: 180px; background: var(--paper); }

  .contact { position: absolute; left: 48px; top: 930px; color: var(--ink); font-weight: 500; font-size: 16.5px; line-height: 21.5px; }
  .contact li { list-style: none; display: flex; gap: 10px; align-items: flex-start; }
  .contact svg { flex: 0 0 16px; margin-top: 3px; }

  .speaker-art {
    position: absolute; left: 430px; top: 405px; width: 330px; height: 671px;
    border-radius: 260px 0 0 0;
    background: linear-gradient(180deg, #f08a1c 0%, #e9761c 30%, #c9441f 60%, #8a2a14 100%);
  }

  .speaker-badge {
    position: absolute; left: 324px; top: 835px; width: 170px; height: 170px; border-radius: 50%;
    background: var(--white); border: 1.5px solid var(--orange);
    text-align: center; padding-top: 30px;
  }
  .speaker-badge .role {
    display: inline-block; background: var(--orange); color: var(--white);
    font-weight: 700; font-size: 9px; letter-spacing: 1.5px; padding: 2px 18px; border-radius: 8px;
  }
  .speaker-badge .speaker-name {
    font-weight: 900; font-size: 23px; line-height: 22px; color: var(--navy); margin-top: 4px;
  }
</style>
</head>
<body>
  <main class="flyer">
    <div class="speaker-art" role="img" aria-label="Speaker Prophet Marcus Olunde in a red blazer before an orange flame backdrop"></div>

    <svg class="flyer-shapes" viewBox="0 0 760 1076" aria-hidden="true">
      <g stroke="#ffffff" stroke-width="1.5" fill="#ffffff">
        <line x1="20" y1="335" x2="96" y2="335"/><circle cx="20" cy="335" r="4"/>
        <polyline points="252,335 265,347 300,347" fill="none"/>
        <circle cx="256" cy="347" r="4"/><circle cx="294" cy="335" r="4"/>
        <polyline points="456,347 490,335 505,335" fill="none"/>
        <circle cx="460" cy="335" r="4"/><circle cx="500" cy="347" r="4"/>
        <line x1="660" y1="335" x2="736" y2="335"/><circle cx="736" cy="335" r="4"/>
      </g>
      <g fill="none" stroke="#ffffff" stroke-width="1">
        <path d="M96,335 A78,78 0 0 1 252,335"/>
        <path d="M300,347 A78,78 0 0 0 456,347"/>
        <path d="M505,335 A78,78 0 0 1 660,335"/>
      </g>
      <g fill="#e67a1c" stroke="#ffffff" stroke-width="5">
        <circle cx="174" cy="340" r="66"/>
        <circle cx="378" cy="352" r="66"/>
        <circle cx="582" cy="340" r="66"/>
      </g>
      <g fill="#ffffff">
        <path d="M152,318 Q174,300 196,318 Q174,336 152,318 Z"/>
        <circle cx="174" cy="318" r="6" fill="#e67a1c"/>
        <path d="M378,300 C392,314 398,326 392,338 C388,346 368,346 364,338 C360,328 368,322 370,314 C374,322 376,324 378,322 C382,316 380,308 378,300 Z"/>
      </g>
      <g fill="none" stroke="#ffffff" stroke-width="4">
        <path d="M602,318 A20,20 0 1 1 596,304"/>
        <circle cx="582" cy="314" r="5"/>
        <path d="M573,328 Q582,320 591,328"/>
      </g>
      <path d="M596,296 L604,305 L592,308 Z" fill="#ffffff"/>

      <g fill="none" stroke="#ffffff" stroke-width="3" stroke-linecap="round">
        <path d="M329,872 A100,100 0 0 1 460,826"/>
        <path d="M490,860 A100,100 0 0 1 470,1000"/>
        <path d="M420,1020 A100,100 0 0 1 330,985"/>
      </g>
    </svg>

    <h1 class="event-title">KESTREL</h1>
    <div class="title-bar">
      <span class="summit">SUMMIT</span>
      <span class="year">2020</span>
    </div>

    <span class="focus-label" style="left:104px; top:370px;">PROPHETIC</span>
    <span class="focus-label" style="left:308px; top:382px;">FIRE</span>
    <span class="focus-label" style="left:512px; top:370px;">REVIVAL</span>

    <p class="theme">IN FIRE<br>AND ON FIRE</p>
    <div class="divider"></div>

    <section class="schedule">
      <h2>TIME AND DATE OF EVENT</h2>
      <p>Thursday December 31st @ <strong>6:30PM</strong></p>
      <p>Friday January 1st @ <strong>6:30PM</strong></p>
      <p>Saturday 2nd @ <strong>6:30PM</strong></p>
      <p>Sunday 3rd @ <strong>4:30PM</strong></p>
    </section>

    <div class="host"><span class="mark"></span><span class="name">HALVERN</span></div>

    <div class="footer-band" style="width:430px"></div>

    <ul class="contact">
      <li>
        <svg width="16" height="16" viewBox="0 0 16 16"><circle cx="8" cy="8" r="7" fill="none" stroke="#f08a1c" stroke-width="1.3"/><path d="M5.5,4.5 L7,6 L6.2,7.2 Q7.3,9 8.8,9.8 L10,9 L11.5,10.5 L10.5,11.6 Q6.5,11 4.4,5.5 Z" fill="#f08a1c"/></svg>
        <span>207 583 2914</span>
      </li>
      <li>
        <svg width="16" height="16" viewBox="0 0 16 16"><circle cx="8" cy="8" r="7" fill="#f08a1c"/><rect x="4.2" y="5.2" width="7.6" height="5.6" fill="none" stroke="#ffffff" stroke-width="1"/><path d="M4.2,5.2 L8,8.3 L11.8,5.2" fill="none" stroke="#ffffff" stroke-width="1"/></svg>
        <span>contact@brightmeadowfold.org</span>
      </li>
      <li>
        <svg width="16" height="16" viewBox="0 0 16 16" style="margin-top:24px"><circle cx="8" cy="8" r="7" fill="none" stroke="#f08a1c" stroke-width="1.3"/><path d="M8,12 Q5,8.5 5,6.8 A3,3 0 0 1 11,6.8 Q11,8.5 8,12 Z" fill="#f08a1c"/><circle cx="8" cy="6.8" r="1.1" fill="#ffffff"/></svg>
        <span>Harlow Community Center,<br>239 Fennimore Street,<br>Portland, ME 04117</span>
      </li>
    </ul>

    <div class="speaker-badge">
      <span class="role">SPEAKER</span>
      <p class="speaker-name">PROPHET<br>MARCUS<br>OLUNDE</p>
    </div>
  </main>
</body>
</html>
```